We need a fresh, new church business card!!

We need a church business card with basic info to hand out as invites. We are looking for something clean that communicates our basic information clearly.

We are open to square or rectangle card sizes.

The attached logo is the only one that I have available. We'd like to see options with with text of the logo lighter and on a dark background as well as options with white/light backgrounds.

Also, we'd like to see option with rounded corners.

• Address - 2738 Larkmoor Ave., Rockford, IL 61109
• Website - brookvale.church
• Phone - 815-392-6157
• Service times -
• Sunday - 10am Sunday School
• - 11am Family Worship
• - 6pm Night of Prayer
• Wednesday - 7:30pm Adult Bible Study
• Classes for all ages

```html
<!DOCTYPE html>
<html lang="en">
<head>
<meta charset="utf-8">
<title>Brookvale Pentecostal Church – Business Card</title>
<link rel="stylesheet" href="https://fonts.googleapis.com/css2?family=Source+Sans+3:wght@400;600;700&display=swap">
<style>
  :root {
    --teal: #5394a5;
    --teal-text: #4b8fa1;
    --white: #ffffff;
    --ink: #5d5f61;
    --grey: #6b6d70;
    --page: #ecedee;
  }
  * { box-sizing: border-box; margin: 0; padding: 0; }
  html, body { width: 1200px; height: 1200px; overflow: hidden; }
  body {
    background: var(--page);
    font-family: "Source Sans 3", sans-serif;
    display: flex;
    flex-direction: column;
    align-items: center;
    justify-content: center;
    gap: 60px;
  }
  .card {
    width: 840px;
    height: 480px;
    position: relative;
    box-shadow: 0 6px 18px rgba(0,0,0,0.15);
    overflow: hidden;
  }

  /* Front */
  .card-front { background: var(--teal); color: var(--white); }
  .brand {
    display: flex;
    align-items: center;
    gap: 24px;
  }
  .brand-dot {
    width: 96px; height: 96px; border-radius: 50%;
    flex: none;
  }
  .brand-name {
    font-weight: 600;
    line-height: 1;
    letter-spacing: 0.02em;
  }
  .brand-name .main { display: block; font-size: 62px; letter-spacing: 0.01em; }
  .brand-name .sub { display: block; font-size: 21px; letter-spacing: 0.24em; margin-top: 8px; }

  .card-front .brand {
    position: absolute; left: 50%; top: 200px; transform: translate(-50%, -50%);
    color: var(--white);
  }
  .card-front .brand-dot { background: var(--white); }
  .website {
    position: absolute; bottom: 30px; left: 0; right: 0;
    text-align: center; font-size: 22px;
  }
  .website strong { font-weight: 700; }

  /* Back */
  .card-back { background: var(--white); display: flex; }
  .service-panel {
    width: 310px; height: 100%;
    background: var(--teal); color: var(--white);
    text-align: center;
    padding: 52px 24px 0;
  }
  .service-title { font-size: 30px; font-weight: 700; margin-bottom: 10px; }
  .service-day { font-size: 24px; font-weight: 700; line-height: 1.1; margin-top: 6px; }
  .service-list { list-style: none; font-size: 20px; line-height: 1.18; }
  .divider { border: 0; border-top: 1.5px solid var(--white); margin: 22px 8px 18px; }
  .pin { width: 22px; height: 28px; display: block; margin: 0 auto 12px; }
  .address { font-size: 20px; line-height: 1.25; font-style: normal; }

  .contact-side { flex: 1; position: relative; color: var(--ink); }
  .card-back .brand {
    position: absolute; left: 50px; top: 70px;
    color: var(--ink);
  }
  .card-back .brand-dot { background: var(--teal); width: 88px; height: 88px; }
  .card-back .brand-name .main { font-size: 56px; }
  .card-back .brand-name .sub { font-size: 19px; }

  .person { position: absolute; left: 0; right: 0; top: 220px; text-align: center; }
  .person-name { font-size: 32px; font-weight: 700; color: var(--teal-text); line-height: 1; }
  .person-role { font-size: 19px; color: var(--grey); margin-top: 4px; }

  .direct {
    position: absolute; right: 36px; top: 300px;
    list-style: none; text-align: right; font-size: 20px; line-height: 1.35;
  }
  .direct li, .social li { display: flex; align-items: center; gap: 10px; }
  .direct li { justify-content: flex-end; }
  .icon { width: 18px; height: 18px; flex: none; }

  .social {
    position: absolute; left: 30px; top: 382px;
    list-style: none; font-size: 20px; line-height: 1.35;
  }
  .social-mark { width: 16px; height: 16px; background: var(--teal); border-radius: 2px; flex: none; }
</style>
</head>
<body>

  <section class="card card-front" aria-label="Card front">
    <div class="brand">
      <span class="brand-dot"></span>
      <span class="brand-name"><span class="main">BROOKVALE</span><span class="sub">PENTECOSTAL CHURCH</span></span>
    </div>
    <p class="website">www.<strong>brookvale</strong>.church</p>
  </section>

  <section class="card card-back" aria-label="Card back">
    <aside class="service-panel">
      <h2 class="service-title">Service Times</h2>
      <h3 class="service-day">Sunday</h3>
      <ul class="service-list">
        <li>10am Sunday School</li>
        <li>11am Family Worship</li>
        <li>6pm Night of Prayer</li>
      </ul>
      <h3 class="service-day">Wednesday</h3>
      <ul class="service-list">
        <li>7:30pm Adult Bible Study</li>
        <li>Classes for all ages</li>
      </ul>
      <hr class="divider">
      <svg class="pin" viewBox="0 0 22 28" aria-hidden="true">
        <path d="M11 1.5a9 9 0 0 0-9 9c0 6.5 9 16 9 16s9-9.5 9-16a9 9 0 0 0-9-9z" fill="none" stroke="#fff" stroke-width="2.2"/>
        <circle cx="11" cy="10.5" r="3.2" fill="#fff"/>
      </svg>
      <address class="address">2738 Larkmoor Ave.<br>Rockford, IL 61109</address>
    </aside>

    <div class="contact-side">
      <div class="brand">
        <span class="brand-dot"></span>
        <span class="brand-name"><span class="main">BROOKVALE</span><span class="sub">PENTECOSTAL CHURCH</span></span>
      </div>

      <div class="person">
        <p class="person-name">Marcus Ellery</p>
        <p class="person-role">Lead Pastor</p>
      </div>

      <ul class="direct">
        <li>815-392-6157
          <svg class="icon" viewBox="0 0 18 18" aria-hidden="true">
            <path d="M2 6c0-2 3-3.5 7-3.5S16 4 16 6v1.5h-3.5V5.8H5.5v1.7H2z" fill="#5394a5"/>
            <path d="M4 9h10l1.5 6.5h-13z" fill="#5394a5"/>
            <circle cx="9" cy="12" r="1.8" fill="#fff"/>
          </svg>
        </li>
        <li>m.ellery@brookvale.church
          <svg class="icon" viewBox="0 0 18 18" aria-hidden="true">
            <rect x="1" y="3.5" width="16" height="11" rx="1" fill="#5394a5"/>
            <path d="M1.5 4.5 9 10l7.5-5.5" fill="none" stroke="#fff" stroke-width="1.4"/>
          </svg>
        </li>
      </ul>

      <ul class="social">
        <li><span class="social-mark"></span>/brookvale.church</li>
        <li><span class="social-mark"></span>@_brookvale</li>
      </ul>
    </div>
  </section>

</body>
</html>
```